2 x Digitize Logo | 2 x Business Cards | 2 x Fridge Magnets

We require 6 deliverables:
1. Residential logo redrawn (same just high quality for large print format).
2. Corporate logo redrawn (minor changes to wording and high quality for large print format).
3. New business card design for Furniture Removals (residential)
4. New business card design for Corporate Relocations (business)
5. New Fridge magnet for Furniture removals (residential)
6. New fridge magnet for Corporate Relocations (business)
1. Residential Logo
a. We require the logo to be translated into a high quality digital image with no modifications.
(see attached resilogo.jpg)
2. Residential Logo
a. We require the logo to be edited (add the word corporate relocations) be translated into a high quality digital image.
(see attached corplogo.jpg)
3. Using the resilogo please make a new business card for our business.
a. Please see the web site https://www.bluegatehaulage.com.au for colours and inspiration.
b. The residential business card needs the following information:
i. Business Name (using the residential logo).
ii. Free Call: 1800 BG Haul (the B, G and Haul much be the same colour as the logo).
iii. Website: www.BluegateHaulage.com.au
iv. Address: 4/6 Marlow Court, VIC 3201
v. Email: move@BluegateHaulage.com.au
vi. backof Card:
Review our service
www.TellTallyHub.com.au
Services: Local, Country, Interstate | Furniture Removals | Piano, Billiard Tables & Antiques
4. Using the corplogo please make a new business card for our business.
b. The corporate business card needs the following information:
i. Business Name (using the corporate logo).
v. Email: corporate@BluegateHaulage.com.au
vi. Back of Card:
Review our service
www.TellTallyHub.com.au
Services: Corporate relocations | Office equipment moves | Packing Service | Packing Materials
5. Using the resilogo please make a new fridge magent for our business.
b. The residential fidge magnet needs the following information:
iv. Services: Local, Country, Interstate | Furniture Removals | Piano, Billiard Tables & Antiques
6. Using the corplogo please make a new fridge magent for our business.
b. The corporate fidge magnet needs the following information:
iv. Services: Local, Country, Interstate | Corporate relocations
Target Market(s)
Residential Furniture Removals and Corporate Office relocations
Industry/Entity Type
Business
Contact Information for Business Card
Please see full brief for six items required
Requirements
Must have
- Clean simple, easy to read
Nice to have
- fresh, stand out, eye catching
Should not have
- plain, standard, boring, general

```html
<!DOCTYPE html>
<html lang="en">
<head>
<meta charset="utf-8">
<title>Bluegate Haulage – Corporate Business Card</title>
<link rel="stylesheet" href="https://fonts.googleapis.com/css2?family=Open+Sans:wght@400;600&family=Oswald:wght@600;700&display=swap">
<style>
  :root {
    --stage: #1b1b1b;
    --card-dark: #2c2c2c;
    --card-edge: #3a3a3a;
    --card-light: #f3f3f3;
    --ink: #555555;
    --ink-light: #a8a8a8;
    --yellow: #e8b51a;
    --red: #d9262e;
    --green: #2e9e48;
    --ghost: #353535;
  }
  * { margin: 0; padding: 0; box-sizing: border-box; }
  html, body { width: 1200px; height: 716px; overflow: hidden; }
  body {
    background: var(--stage);
    font-family: "Open Sans", Arial, sans-serif;
    position: relative;
  }
  .card {
    position: absolute;
    top: 200px;
    width: 540px;
    height: 310px;
    border-radius: 18px;
    overflow: hidden;
    box-shadow: 0 10px 28px rgba(0, 0, 0, 0.55);
  }

  /* ---------- back of card ---------- */
  .card-back {
    left: 30px;
    background: var(--card-dark);
    border: 1px solid var(--card-edge);
    color: var(--ink-light);
  }
  .ghost-name {
    position: absolute; right: 26px; top: 174px;
    font-family: "Oswald", sans-serif; font-weight: 700;
    font-size: 36px; letter-spacing: 1px; color: var(--ghost);
    white-space: nowrap; line-height: 1;
  }
  .services { position: absolute; left: 36px; top: 28px; }
  .services-title { color: var(--yellow); font-size: 15px; margin-bottom: 8px; }
  .service-list { list-style: none; }
  .service-list li {
    display: flex; align-items: center; gap: 8px;
    font-size: 15px; color: var(--ink-light); margin-bottom: 7px;
  }
  .service-list svg { width: 16px; height: 14px; flex: none; }
  .review { position: absolute; left: 36px; top: 196px; }
  .review-title { color: var(--green); font-size: 13px; }
  .review-url { color: #b0b0b0; font-size: 14px; margin-top: 3px; }

  .brand {
    position: absolute; display: flex; align-items: center; gap: 8px;
    font-family: "Oswald", sans-serif; font-weight: 700;
    color: var(--green); text-transform: uppercase; white-space: nowrap;
    line-height: 1.2;
  }
  .brand-dot { width: 14px; height: 14px; border-radius: 50%; background: var(--green); }
  .card-back .brand { right: 26px; bottom: 24px; font-size: 32px; }

  /* ---------- front of card ---------- */
  .card-front {
    left: 630px;
    background: linear-gradient(135deg, #f7f7f7 0%, #e9e9e9 100%);
    color: var(--ink);
  }
  .holder { position: absolute; left: 28px; top: 22px; display: flex; gap: 10px; }
  .holder-bar { width: 10px; height: 44px; background: var(--yellow); }
  .holder-name { font-size: 22px; color: #666; line-height: 1.1; }
  .holder-role { font-size: 13px; color: var(--green); }
  .card-front .brand { right: 28px; top: 88px; font-size: 34px; }
  .freecall {
    position: absolute; left: 28px; top: 138px;
    font-family: "Oswald", sans-serif; font-weight: 600; font-size: 24px;
    line-height: 1.3;
  }
  .freecall-label { color: var(--yellow); }
  .freecall-number { color: var(--red); font-weight: 700; }
  .contacts { position: absolute; left: 28px; top: 182px; list-style: none; }
  .contacts li { display: flex; align-items: center; gap: 8px; font-size: 14px; color: #555; margin-bottom: 4px; }
  .contacts svg { width: 14px; height: 14px; flex: none; }
  .website { position: absolute; left: 28px; top: 234px; font-size: 15px; color: var(--green); }
  .accent-line { position: absolute; left: 0; top: 0; width: 540px; height: 310px; }
</style>
</head>
<body>

<section class="card card-back">
  <div class="ghost-name" aria-hidden="true">BLUEGATE HAULAGE</div>
  <div class="services">
    <p class="services-title">Services</p>
    <ul class="service-list">
      <li><svg viewBox="0 0 16 14"><path d="M1 7l5 5L15 1" fill="none" stroke="#d9262e" stroke-width="3"/></svg>Corporate relocations</li>
      <li><svg viewBox="0 0 16 14"><path d="M1 7l5 5L15 1" fill="none" stroke="#d9262e" stroke-width="3"/></svg>Office equipment moves</li>
      <li><svg viewBox="0 0 16 14"><path d="M1 7l5 5L15 1" fill="none" stroke="#d9262e" stroke-width="3"/></svg>Packing Service</li>
      <li><svg viewBox="0 0 16 14"><path d="M1 7l5 5L15 1" fill="none" stroke="#d9262e" stroke-width="3"/></svg>Packing Materials</li>
    </ul>
  </div>
  <div class="review">
    <p class="review-title">Review our service</p>
    <p class="review-url">www.TellTallyHub.com.au</p>
  </div>
  <div class="brand"><span class="brand-dot"></span>Bluegate Haulage</div>
</section>

<section class="card card-front">
  <svg class="accent-line" viewBox="0 0 540 310" aria-hidden="true">
    <line x1="0" y1="272" x2="360" y2="272" stroke="#d9262e" stroke-width="2"/>
    <polygon points="360,271 378,265 540,265 540,277 360,273" fill="#d9262e"/>
  </svg>
  <div class="holder">
    <span class="holder-bar"></span>
    <div>
      <p class="holder-name">Your Name</p>
      <p class="holder-role">Position</p>
    </div>
  </div>
  <div class="brand"><span class="brand-dot"></span>Bluegate Haulage</div>
  <p class="freecall"><span class="freecall-label">Free Call:</span> <span class="freecall-number">1800 BG</span></p>
  <ul class="contacts">
    <li><svg viewBox="0 0 14 14"><path d="M7 0a5 5 0 0 0-5 5c0 4 5 9 5 9s5-5 5-9a5 5 0 0 0-5-5zm0 7a2 2 0 1 1 0-4 2 2 0 0 1 0 4z" fill="#2e9e48"/></svg>4/6 Marlow Court, VIC 3201</li>
    <li><svg viewBox="0 0 14 14"><rect x="0" y="3" width="14" height="9" fill="#2e9e48"/><path d="M0 3l7 5 7-5" fill="none" stroke="#f3f3f3" stroke-width="1.2"/></svg>corporate@BluegateHaulage.com.au</li>
  </ul>
  <p class="website">www.BluegateHaulage.com.au</p>
</section>

</body>
</html>
```